Morvela Aesthetic Doctor

I require an elegant, luxurious looking business card for my aesthetic business. I am a doctor and that will set me aside from competitors. I am planning to provide home and spa based treatments to clients with high expectations. I have attached my logo.

```html
<!DOCTYPE html>
<html lang="en">
<head>
<meta charset="utf-8">
<title>Morvela Aesthetic Doctor – Business Card</title>
<link rel="stylesheet" href="https://fonts.googleapis.com/css2?family=Cinzel:wght@400&family=Open+Sans:ital,wght@0,400;0,600;1,600&display=swap">
<style>
  :root {
    --stage: #3b3b3b;
    --card: #ffffff;
    --brand-grey: #9c9c9c;
    --sky: #1fa8e6;
    --ocean: #0f6db8;
    --ink-light: #ffffff;
    --ink-muted: #4a4a4a;
  }
  * { box-sizing: border-box; margin: 0; padding: 0; }
  html, body { width: 1200px; height: 801px; overflow: hidden; }
  body {
    background: var(--stage);
    font-family: "Open Sans", Arial, sans-serif;
    position: relative;
  }
  .card {
    position: absolute;
    top: 274px;
    width: 448px;
    height: 254px;
    background: var(--card);
    border-radius: 16px;
    overflow: hidden;
    box-shadow: 0 6px 18px rgba(0,0,0,.35);
  }
  .card--front { left: 128px; }
  .card--back { left: 624px; }
  .card__waves { position: absolute; inset: 0; width: 100%; height: 100%; }
  .wave-light { fill: var(--sky); }
  .wave-deep { fill: var(--ocean); }

  .brand {
    position: absolute;
    display: flex;
    align-items: center;
    gap: 12px;
    color: var(--brand-grey);
    font-family: "Cinzel", Georgia, serif;
    font-weight: 400;
    line-height: 1.05;
  }
  .brand__dot {
    border-radius: 50%;
    border: 2px solid var(--brand-grey);
    flex: none;
  }
  .card--front .brand { left: 60px; top: 40px; }
  .card--front .brand__dot { width: 70px; height: 70px; }
  .card--front .brand__name { font-size: 44px; letter-spacing: 1px; }
  .card--front .brand__tag { font-size: 17px; letter-spacing: 1.5px; }
  .card--back .brand { left: 22px; top: 20px; gap: 10px; }
  .card--back .brand__dot { width: 52px; height: 52px; }
  .card--back .brand__name { font-size: 32px; letter-spacing: 1px; }
  .card--back .brand__tag { font-size: 13px; letter-spacing: 1.2px; }

  .tagline {
    position: absolute;
    right: 34px;
    bottom: 40px;
    color: var(--ink-light);
    font-style: italic;
    font-weight: 600;
    font-size: 14px;
  }

  .doctor {
    position: absolute;
    right: 14px;
    top: 104px;
    text-align: right;
  }
  .doctor__name {
    font-family: "Cinzel", Georgia, serif;
    color: var(--sky);
    font-size: 20px;
    letter-spacing: .5px;
  }
  .doctor__cred {
    color: var(--ink-muted);
    font-size: 8px;
    line-height: 1.6;
  }

  .services {
    position: absolute;
    left: 12px;
    top: 203px;
    color: var(--ink-light);
    font-size: 9.5px;
    line-height: 1.6;
    list-style: none;
  }
  .contact {
    position: absolute;
    left: 290px;
    top: 206px;
    color: var(--ink-light);
    font-size: 9.5px;
    line-height: 1.6;
    list-style: none;
  }
  .contact li { display: flex; align-items: center; gap: 8px; }
  .contact svg { width: 8px; height: 8px; fill: var(--ink-light); }
  .social {
    position: absolute;
    right: 16px;
    top: 210px;
    display: flex;
    flex-direction: column;
    gap: 8px;
  }
  .social span {
    width: 12px; height: 12px;
    border-radius: 50%;
    background: var(--ink-light);
  }
</style>
</head>
<body>

<section class="card card--front" aria-label="Business card front">
  <svg class="card__waves" viewBox="0 0 448 254" preserveAspectRatio="none" aria-hidden="true">
    <path class="wave-light" d="M0,205 C120,172 260,142 448,128 L448,142 C260,156 120,186 0,219 Z"/>
    <path class="wave-deep" d="M0,229 C120,196 260,166 448,152 L448,254 L0,254 Z"/>
  </svg>
  <div class="brand">
    <span class="brand__dot"></span>
    <div>
      <div class="brand__name">MORVELA</div>
      <div class="brand__tag">AESTHETIC DOCTOR</div>
    </div>
  </div>
  <p class="tagline">Home &amp; Spa Based Treatments</p>
</section>

<section class="card card--back" aria-label="Business card back">
  <svg class="card__waves" viewBox="0 0 448 254" preserveAspectRatio="none" aria-hidden="true">
    <path class="wave-light" d="M0,168 C90,140 200,135 300,158 C370,174 420,168 448,160 L448,174 C410,184 360,186 300,174 C200,152 100,152 0,182 Z"/>
    <path class="wave-deep" d="M0,196 C100,168 200,166 300,186 C370,199 420,196 448,188 L448,254 L0,254 Z"/>
  </svg>
  <div class="brand">
    <span class="brand__dot"></span>
    <div>
      <div class="brand__name">MORVELA</div>
      <div class="brand__tag">AESTHETIC DOCTOR</div>
    </div>
  </div>
  <div class="doctor">
    <h1 class="doctor__name">Dr. Elise Varkon</h1>
    <p class="doctor__cred">MRCPCH MD<br>Australasian Diploma of Aesthetic Medicine</p>
  </div>
  <ul class="services">
    <li>Dermal Injectables - Plasma Facials - Microneedling</li>
    <li>Skin Boosters - Excessive Sweating</li>
    <li>Home &amp; Spa Based Treatments</li>
  </ul>
  <ul class="contact">
    <li><svg viewBox="0 0 10 10"><path d="M2,0 L4,2.5 L3,3.5 C4,5.5 5,6.5 6.5,7 L7.5,6 L10,8 L8.5,10 C4,9.5 0.5,6 0,1.5 Z"/></svg>0800 555 014</li>
    <li><svg viewBox="0 0 10 10"><path d="M0,2 H10 V8.5 H0 Z M0,2 L5,5.5 L10,2" stroke="#0f6db8" stroke-width="0.8"/></svg>elise@morvela.co.nz</li>
    <li><svg viewBox="0 0 10 10"><circle cx="5" cy="5" r="5"/></svg>www.morvela.co.nz</li>
  </ul>
  <div class="social" aria-hidden="true"><span></span><span></span></div>
</section>

</body>
</html>
```